Luxury Linden Court/academy - Webdesign

We want to develop a cutting edge website for a luxury tennis academy. Academy is based in Russia and includes all the necessary amenities for comfortable stay: apartments, spa, tennis courts, training facilities, etc.
We would like to see a clean, simple and modern design (with implementation of all the current trends in web design, although our project has to be distinct and unique).
Color scheme: we would like to see colors present in our logos and all the current associated with tennis. We are open to your ideas and creativity on this front.
The final design should communicate simplicity, be user friendly and convey premium feel.
We woud like to see unique ideas in the design, unconventional techniques, etc.
We don't want standard template design!
Updates
We want to mention that this Tennis Academy has a light focus on nature, as the new material we have uploaded illustrates.
Additional comment to everyone!
We couldn't upload this file to the system: it is too big.
Thank you everyone for your submissions!
Industry/Entity Type
Training
Requirements
Must have
- We would like to see the designs for the following pages:
Home Page:
- Slideshow
- Short description and all the standard stuff
About Us:
- Description with some images
Services:
- Simple description of all of the provided services and possibility to book all of them on the website
! Important ! Develop small system for booking of the days of stay and registration for the courses
Booking and registration !
News:
- Creative layout to display recent news of the academy
Coaches:
- Image and short description of our staff.
Club / Gallery:
- Images and descriptions of the amenities in the territory.
We want a unique display of images: not just lines and rows filled with images
- One idea: an interactive map that displays images and description on mouseover or click on the object on the map (but again, we are open to all your ideas)
Contacts:
- Contact form, contacts, etc.
Sport Store:
- Basic layout for the goods and services provided by the sports store located in the academy
Prices:
- Price lists and ranges with a button leading to registration and booking
For pages like About Us and Services, it would be enough to develop one unified layout for all of them.

```html
<!DOCTYPE html>
<html lang="en">
<head>
<meta charset="utf-8">
<title>Linden Court Academy</title>
<link rel="stylesheet" href="https://fonts.googleapis.com/css2?family=Exo+2:wght@400;600;700&family=Arimo:wght@400;700&display=swap">
<style>
:root{
  --green:#1f8a3a;
  --green-dark:#156b2b;
  --lime:#8fc31f;
  --nav:#23382b;
  --paper:#f2efea;
  --ink:#1c1c1c;
  --body:#333;
  --footer:#121212;
  --footer-line:#333;
  --muted:#8a8a8a;
  --white:#fff;
  --fb:#2d4a8a;
}
*{box-sizing:border-box;margin:0;padding:0}
html,body{width:900px;height:1200px;overflow:hidden}
body{position:relative;background:
  radial-gradient(ellipse 420px 260px at 720px 600px,rgba(255,255,255,.55),transparent 70%),
  radial-gradient(ellipse 500px 300px at 120px 860px,rgba(255,255,255,.5),transparent 70%),
  linear-gradient(#efebe5,#f4f1ec 40%,#ece8e2);
  font-family:"Arimo",Arial,sans-serif;color:var(--body)}
.abs{position:absolute}

/* header */
.site-header{left:0;top:0;width:900px;height:86px;background:linear-gradient(#fafaf8,#f1f1ee);border-top:3px solid #6b5a45}
.brand{left:84px;top:22px;display:flex;align-items:center;gap:8px}
.brand-name{font-family:"Exo 2",sans-serif;font-weight:700;font-size:30px;color:var(--green);letter-spacing:-.5px}
.brand-dot{width:32px;height:32px;border-radius:50%;background:var(--lime)}
.connect{left:686px;top:19px;font-family:"Exo 2",sans-serif;font-size:12px;color:var(--green);letter-spacing:.5px}
.connect svg{vertical-align:middle;margin-left:6px}
.social{left:686px;top:40px;display:flex;gap:7px}
.social span{width:29px;height:29px;border-radius:50%;background:linear-gradient(#9a9a9a,#6d6d6d);box-shadow:0 1px 2px rgba(0,0,0,.3)}
.social span:first-child{background:linear-gradient(#3b6bb5,#244c8c)}

/* nav */
.main-nav{left:0;top:86px;width:900px;height:29px;background:linear-gradient(#2a4233,#1e3226);display:flex;align-items:center;padding-left:82px}
.main-nav a{font-size:9.5px;font-weight:700;color:var(--white);text-decoration:none;letter-spacing:.3px;margin-right:33px;line-height:29px}
.main-nav a.active{background:var(--white);color:var(--nav);padding:0 12px;margin-right:22px;position:relative}
.main-nav a.active::after{content:"";position:absolute;left:50%;bottom:-5px;margin-left:-5px;border:5px solid transparent;border-bottom:0;border-top-color:var(--white)}

/* hero */
.hero{left:0;top:115px;width:900px;height:411px;overflow:hidden;background:
  radial-gradient(ellipse 140px 200px at 700px 230px,rgba(214,58,110,.55),transparent 70%),
  radial-gradient(ellipse 90px 130px at 420px 150px,rgba(214,80,120,.35),transparent 70%),
  radial-gradient(ellipse 120px 240px at 790px 120px,rgba(40,70,30,.55),transparent 70%),
  radial-gradient(ellipse 300px 160px at 250px 300px,rgba(150,200,70,.5),transparent 70%),
  linear-gradient(180deg,#4e6b3c 0%,#6a9a3a 30%,#7fb043 55%,#79a447 78%,#b08e74 92%,#c9a991 100%)}
.hero::before{content:"";position:absolute;inset:0;background:
  linear-gradient(90deg,rgba(0,0,0,.28) 0,transparent 35%,transparent 75%,rgba(0,0,0,.15) 100%)}
.hero::after{content:"";position:absolute;inset:0;background:linear-gradient(180deg,rgba(255,255,255,.08),transparent 40%,rgba(0,0,0,.12))}
.hero-title{left:78px;top:186px;font-family:"Exo 2",sans-serif;font-weight:700;font-size:28px;line-height:36px;letter-spacing:1px;color:var(--white);text-shadow:0 2px 5px rgba(0,0,0,.55);white-space:nowrap}
.book-btn{left:80px;top:354px;width:177px;height:44px;background:linear-gradient(#2fa852,#137a2d);border:2px solid #cfe9d2;border-radius:4px;color:var(--white);font-family:"Exo 2",sans-serif;font-weight:700;font-size:22px;letter-spacing:.5px;display:flex;align-items:center;justify-content:center;box-shadow:0 3px 8px rgba(0,0,0,.35);text-shadow:0 1px 2px rgba(0,0,0,.4)}
.dots{left:481px;top:480px;display:flex;gap:5px}
.dots span{width:14px;height:14px;border-radius:50%;border:2px solid var(--white);background:var(--lime);box-shadow:0 1px 2px rgba(0,0,0,.4)}
.dots span:first-child{background:#333}

/* service cards */
.service h3{font-family:"Exo 2",sans-serif;font-weight:600;font-size:21px;letter-spacing:.5px;color:var(--ink);margin-bottom:9px}
.service .thumb{width:230px;height:84px;border:2px solid #b9b9b9;position:relative;box-shadow:0 2px 5px rgba(0,0,0,.18)}
.service .thumb::after{content:"";position:absolute;inset:0;background:linear-gradient(180deg,rgba(255,255,255,.15),transparent 50%,rgba(0,0,0,.12))}
.service .go{position:absolute;right:-11px;bottom:-11px;width:27px;height:27px;border-radius:50%;background:radial-gradient(circle at 40% 35%,#b5e04a,#5f9a12);border:2px solid var(--white);display:flex;align-items:center;justify-content:center;z-index:2;box-shadow:0 1px 3px rgba(0,0,0,.4)}

/* welcome */
.welcome{left:79px;top:696px;width:480px}
.welcome h1{font-family:"Exo 2",sans-serif;font-weight:700;font-size:23px;letter-spacing:.8px;color:var(--ink);margin-bottom:22px}
.welcome p{font-size:10.4px;line-height:18px;letter-spacing:.55px;margin-bottom:18px}

/* tabs */
.tabs{left:597px;top:700px;display:flex;gap:4px}
.tabs span{width:71px;height:22px;border:1px solid #ccc;border-bottom:none;background:#e8e6e2;font-family:"Exo 2",sans-serif;font-size:14px;color:#333;display:flex;align-items:center;justify-content:center}
.tabs span.on{background:var(--white);height:23px;position:relative;z-index:2}
.tab-panel{left:585px;top:721px;width:242px;height:195px;background:var(--white);border:1px solid #ccc;padding:15px 14px;box-shadow:0 1px 4px rgba(0,0,0,.08)}
.event{display:flex;gap:10px;padding-bottom:9px;margin-bottom:12px;border-bottom:1px solid #ddd}
.event .pic{width:52px;height:55px;flex:none;border:3px solid #fff;outline:1px solid #ccc}
.event h4{font-size:11.5px;color:var(--green);font-weight:400;line-height:13px;letter-spacing:.3px;margin-bottom:3px}
.event p{font-size:8.6px;line-height:10.5px;color:#333;letter-spacing:.2px}
.event time{display:block;font-size:8.6px;margin-top:3px}
.view-all{position:absolute;right:18px;bottom:9px;font-size:10px;color:var(--green-dark);text-decoration:underline}

/* footer */
.site-footer{left:0;top:935px;width:900px;height:265px;background:linear-gradient(#2c2c2c,var(--footer) 35%);border-top:1px dotted #555}
.foot-h{font-family:"Exo 2",sans-serif;font-size:18px;color:#d6d6d6;font-weight:400;letter-spacing:.5px}
.foot-list{left:80px;top:1003px;width:180px;list-style:none}
.foot-list li{font-size:9px;color:var(--muted);border-bottom:1px dashed #444;height:22.5px;line-height:22px;padding-left:14px;position:relative}
.foot-list li::before{content:"›";position:absolute;left:2px}
.gallery{left:322px;top:999px;display:grid;grid-template-columns:102px 102px;gap:12px 11px}
.gallery div{height:62px;box-shadow:0 2px 5px rgba(0,0,0,.6)}
.social-box{left:601px;top:951px;width:225px;height:198px;background:var(--white);padding:7px 8px;font-size:8px;color:#333}
.sb-head{display:flex;gap:7px;align-items:flex-start}
.sb-head .sq{width:36px;height:36px;background:#e4ecd6;display:flex;align-items:center;justify-content:center}
.sb-head .sq i{width:24px;height:24px;border-radius:50%;background:var(--lime)}
.sb-head b{font-size:10.5px;color:var(--fb)}
.like{display:inline-block;border:1px solid #aab;padding:1px 4px;margin-top:5px;margin-right:4px;color:var(--fb);font-size:7.5px}
.fans{display:grid;grid-template-columns:repeat(5,37px);column-gap:4px;row-gap:2px;margin-top:5px;padding-left:3px}
.fans figure{text-align:center}
.fans figure div{height:37px}
.fans figcaption{font-size:6.5px;color:#888;line-height:10px}
.sb-foot{margin-top:2px;font-size:7px;color:#777;display:flex;align-items:center;gap:4px}
.sb-foot i{width:9px;height:9px;background:var(--fb)}
.bottom-bar{left:0;top:1169px;width:900px;height:31px;border-top:1px solid var(--footer-line);font-size:8.5px;color:#555;display:flex;justify-content:space-between;align-items:center;padding:0 80px}
</style>
</head>
<body>

<header class="site-header abs">
  <div class="brand abs"><span class="brand-name">Linden Court</span><span class="brand-dot"></span></div>
  <div class="connect abs">Connect with us<svg width="28" height="14" viewBox="0 0 28 14"><path d="M1 5c8-4 18-4 24 5" stroke="#e0453a" fill="none" stroke-width="1.2"/><path d="M21 9l4 2 1-5" stroke="#e0453a" fill="none" stroke-width="1.2"/></svg></div>
  <div class="social abs" aria-label="Social links"><span></span><span></span><span></span><span></span></div>
</header>

<nav class="main-nav abs">
  <a class="active">HOME</a><a>ABOUT US</a><a>SERVICES</a><a>NEWS</a><a>COACHES</a><a>CLUB / GALLERY</a><a>CONTACTS</a><a>SPORT STORE</a><a>PRICES</a>
</nav>

<section class="hero abs" role="img" aria-label="Photo of a young player in a pink jacket returning a ball on an outdoor court behind a chain fence"></section>
<h2 class="hero-title abs">LOREM IPSUM IS SUMPLY<br>DUMMY HEADING FOR THE<br>WEB AND PRINT MEDIA<br>LOREM IS SIMPLY.</h2>
<div class="book-btn abs">BOOK NOW!</div>
<div class="dots abs"><span></span><span></span><span></span><span></span></div>

<div class="service abs" style="left:80px;top:544px">
  <h3>Gym &amp; Training</h3>
  <div class="thumb" role="img" aria-label="Photo of a coach training kids with exercise balls in a gym" style="background:radial-gradient(ellipse 40px 20px at 60px 75px,#8a4aa0,transparent 80%),radial-gradient(ellipse 40px 20px at 150px 78px,#e3a030,transparent 80%),radial-gradient(ellipse 30px 18px at 215px 78px,#e0408a,transparent 80%),linear-gradient(90deg,#d9cfc6,#b29686 35%,#cfc3b8 60%,#a88a78)"><span class="go"><svg width="10" height="10" viewBox="0 0 10 10"><path d="M3 1l4 4-4 4" stroke="#fff" stroke-width="2" fill="none"/></svg></span></div>
</div>
<div class="service abs" style="left:336px;top:546px">
  <h3>Spa</h3>
  <div class="thumb" role="img" aria-label="Photo of a woman receiving a hot stone massage" style="background:radial-gradient(ellipse 150px 30px at 110px 65px,#d99a6a,transparent 80%),linear-gradient(#f3eeea 0%,#eadfd6 40%,#dcb594 75%,#f1ede8 100%)"><span class="go"><svg width="10" height="10" viewBox="0 0 10 10"><path d="M3 1l4 4-4 4" stroke="#fff" stroke-width="2" fill="none"/></svg></span></div>
</div>
<div class="service abs" style="left:591px;top:546px">
  <h3>Horse Riding</h3>
  <div class="thumb" role="img" aria-label="Photo of a young rider on a brown horse against a blue sky" style="background:radial-gradient(ellipse 70px 35px at 120px 65px,#6b3a20,transparent 80%),radial-gradient(ellipse 120px 30px at 80px 30px,rgba(255,255,255,.7),transparent 80%),linear-gradient(#2f6cc0,#6fa6e0 55%,#b9d6f2)"><span class="go"><svg width="10" height="10" viewBox="0 0 10 10"><path d="M3 1l4 4-4 4" stroke="#fff" stroke-width="2" fill="none"/></svg></span></div>
</div>

<section class="welcome abs">
  <h1>Welcome to Linden Court Academy!</h1>
  <p>Lorem ipsum dolor sit amet, consectetuer adipiscing elit, sed diam nonummy nibh euismod tincidunt ut laoreet dolore magna aliquam erat volutpat Lorem ipsum dolor sit amet, consectetuer adipiscing elit, sed diam nonummy nibh euismod tincidunt ut laoreet dolore magna aliquam erat volutpat</p>
  <p>Lorem ipsum dolor sit amet, consectetuer adipiscing elit, sed diam nonummy nibh euismod tincidunt ut laoreet dolore magna aliquam erat volutpat Lorem ipsum dolor sit amet, consectetuer adipiscing elit, sed diam nonummy nibh euismod tincidunt ut laoreet dolore magna aliquam erat volutpat sed.</p>
</section>

<div class="tabs abs"><span class="on">Events</span><span>News</span><span>Posts</span></div>
<aside class="tab-panel abs">
  <div class="event">
    <div class="pic" role="img" aria-label="Gym training photo" style="background:radial-gradient(circle at 30% 70%,#d8403a,transparent 50%),radial-gradient(circle at 70% 75%,#e3a030,transparent 45%),linear-gradient(#cfc2b6,#9c7f6c)"></div>
    <div><h4>Lorem ipsum is simply dummy text</h4><p>Loorem ipsum is simply dummy text content for web</p><time>Dec 16, 2012</time></div>
  </div>
  <div class="event" style="border:none">
    <div class="pic" role="img" aria-label="Horse riding photo" style="background:radial-gradient(circle at 45% 45%,#d9d2c8,transparent 35%),linear-gradient(#3b3029,#6b4a32)"></div>
    <div><h4>Lorem ipsum is simply dummy text</h4><p>Loorem ipsum is simply dummy text content for web</p><time>Dec 16, 2012</time></div>
  </div>
  <a class="view-all">View All Events ▸</a>
</aside>

<footer class="site-footer abs"></footer>
<div class="foot-h abs" style="left:78px;top:962px">Services</div>
<ul class="foot-list abs">
  <li>Tennis</li><li>Horse Riding</li><li>Spa</li><li>Beauty Center</li><li>Forest</li><li>Lorem ipsum</li>
</ul>
<div class="foot-h abs" style="left:321px;top:962px">Photo gallery</div>
<div class="gallery abs">
  <div role="img" aria-label="Photo of players on a clay court" style="background:radial-gradient(ellipse 30px 25px at 30px 30px,#2f55b0,transparent 80%),radial-gradient(ellipse 25px 25px at 65px 30px,#c8302a,transparent 80%),linear-gradient(#9fb4ca,#7d9a5a 45%,#b86a40)"></div>
  <div role="img" aria-label="Photo of guests relaxing outdoors" style="background:radial-gradient(ellipse 25px 30px at 70px 35px,#e0b090,transparent 80%),linear-gradient(#8aa6bd,#6d7d62 55%,#4a3c33)"></div>
  <div role="img" aria-label="Photo of a girl lying among wildflowers" style="background:radial-gradient(ellipse 35px 25px at 60px 35px,#e2c09a,transparent 80%),radial-gradient(circle at 20% 70%,#a05ab0,transparent 30%),linear-gradient(#8a9a3e,#6b7a32)"></div>
  <div role="img" aria-label="Photo of two girls wearing flower wreaths" style="background:radial-gradient(ellipse 22px 26px at 30px 38px,#e8c6a8,transparent 80%),radial-gradient(ellipse 22px 26px at 75px 38px,#e8c6a8,transparent 80%),linear-gradient(#3f8a34,#5f9e3e)"></div>
</div>

<div class="social-box abs">
  <div class="sb-head"><span class="sq"><i></i></span><div><b>Lindencourt</b> <span style="color:var(--fb)">on Friendsphere</span><br><span class="like">Like</span>1,136</div></div>
  <div style="border-top:1px solid #ddd;margin-top:6px;padding-top:5px">1,136 people like <b>Riverside Racquet Club.</b></div>
  <div class="fans">
    <figure><div style="background:#f0f0f0;border:1px solid #ddd"></div><figcaption>Fieldline</figcaption></figure>
    <figure><div style="background:linear-gradient(#9a8c80,#5a4c44)"></div><figcaption>Theo</figcaption></figure>
    <figure><div style="background:linear-gradient(#d8b88a,#a7804e)"></div><figcaption>Dana</figcaption></figure>
    <figure><div style="background:linear-gradient(#6a5aa0,#3b3466)"></div><figcaption>Zara</figcaption></figure>
    <figure><div style="background:linear-gradient(#b7bcc4,#6c7078)"></div><figcaption>Remy</figcaption></figure>
    <figure><div style="background:linear-gradient(#e0c0a8,#b0806a)"></div><figcaption>Alma</figcaption></figure>
    <figure><div style="background:linear-gradient(#c8d0dc,#8a8f96)"></div><figcaption>Arlo</figcaption></figure>
    <figure><div style="background:linear-gradient(#3a3a3a,#8a5a40)"></div><figcaption>Nils</figcaption></figure>
    <figure><div style="background:linear-gradient(#d0d0d0,#9a9a9a)"></div><figcaption>Sven</figcaption></figure>
    <figure><div style="background:linear-gradient(#e8d040,#c8a030)"></div><figcaption>Milo</figcaption></figure>
  </div>
  <div class="sb-foot"><i></i>Friendsphere social plugin</div>
</div>

<div class="bottom-bar abs"><span>Copyright © 2012 Linden Court. All rights reserved.</span><span>Terms and Conditions | Sitemap | RSS</span></div>

</body>
</html>
```